**** Web design project for BoltNet ****

For my ICT company BoltNet I need a website.

We design, build and host web-applications and we have our own CMS product. In the references part we want to show sample websites (thumbnails) + links.

It should look modern (WEB 2.0), rounded corners.

I want the following menu' s:
- Home
- Services
- References
- News
- About BoltNet
- Contact

Sample websites:
See attachments
http://www.vandoqa.com
http://www.greyfoxmanagement.nl

Reason: Want to take some time for feedback and improvements.

Reason: I'm waiting for a black background, with shadow and ambient light. You'll make a good chance!

Industry/Entity Type

It Company

Requirements
Must have
• - Fixed width (1024px), should fit on an IPad2
- Language selection English/Dutch
- Twitter/Facebook/LinkedIn/RSS icons
- Footer for Terms of use and Copyrights
- Search box
- 3 (or more) boxes for information i.e. news, blog or advertisements
Nice to have
• - Footer Site Map
- Contrasting background outside borders
- wide image (rotator) (with transperant sentence block)
- Shadow

```html
<!DOCTYPE html>
<html lang="en">
<head>
<meta charset="utf-8">
<title>BoltNet — Web applications, CMS and hosting</title>
<link rel="stylesheet" href="https://fonts.googleapis.com/css2?family=Arimo:wght@400;700&display=swap">
<style>
:root{
  --blue:#2a9ad8;
  --blue-light:#5cc0f0;
  --blue-dark:#1a6fae;
  --navy:#1d4f8c;
  --btn:#2660a8;
  --ink:#333;
  --muted:#555;
  --line:#d6d6d6;
  --panel:#f1f1f1;
  --page:#fff;
  --bg-top:#d9d9d9;
  --bg-mid:#ececec;
  --bg-dark:#3a3a3a;
  --bg-darker:#262626;
  --red:#d12a1e;
}
*{box-sizing:border-box;margin:0;padding:0}
html,body{width:1050px;height:1200px;overflow:hidden}
body{position:relative;font-family:"Arimo",Arial,sans-serif;color:var(--ink);font-size:10px;
  background:linear-gradient(to bottom,var(--bg-top) 0,#cfcfcf 180px,var(--bg-mid) 180px,var(--bg-mid) 1057px,var(--bg-dark) 1057px,var(--bg-dark) 1167px,var(--bg-darker) 1167px)}
.abs{position:absolute}
.page{position:absolute;left:142px;top:30px;width:768px;height:1062px;background:var(--page);border-radius:6px;box-shadow:0 0 14px rgba(0,0,0,.35)}

/* header */
.account-tab{left:705px;top:30px;width:158px;height:18px;background:var(--blue-dark);border-radius:0 0 8px 8px;color:#fff;font-size:10px;text-align:center;line-height:18px}
.account-tab span{margin:0 4px}
.flags{left:765px;top:57px;display:flex;gap:4px}
.logo-box{left:158px;top:38px;width:337px;height:105px;background:#fff;box-shadow:6px 6px 10px -4px rgba(0,0,0,.25)}
.logo-mark{left:166px;top:47px;width:80px;height:80px;border-radius:50%;background:var(--blue)}
.logo-name{left:262px;top:68px;font-size:42px;color:#6a7178;font-weight:400}
.social{left:610px;top:105px;display:flex;gap:3px}
.social i{display:block;width:22px;height:22px;border-radius:4px}
.search{left:717px;top:104px;width:148px;height:25px;border:1px solid #ccc;border-radius:12px;background:#fff;font-size:10px;font-style:italic;color:#555;padding:6px 10px}
.search svg{position:absolute;right:8px;top:4px}

/* nav */
.main-nav{left:142px;top:150px;width:768px;height:38px;background:linear-gradient(#58c1f2,#1f8fd2);display:flex}
.main-nav a{color:#fff;text-decoration:none;font-size:12px;height:38px;line-height:38px;text-align:center;border-right:1px solid rgba(255,255,255,.35)}

/* slider */
.slider{left:142px;top:190px;width:533px;height:284px;background:#6e8796}
.slide-photo{left:150px;top:198px;width:520px;height:270px;background:linear-gradient(100deg,#dfe7ee 0%,#c2d2de 45%,#7d96ab 70%,#aebfcc 100%)}
.slide-title{left:172px;top:224px;width:300px;font-size:19px;line-height:24px;color:#222;text-align:center}
.slide-text{left:187px;top:274px;width:290px;font-size:11px;line-height:14px;color:#111}
.btn-blue{background:linear-gradient(#4fb4ea,#1f84c8);color:#fff;border-radius:3px;font-size:9px;text-align:center}
.slide-more{left:372px;top:315px;width:60px;height:18px;line-height:18px}
.arrow{width:30px;height:30px;border-radius:50%;background:#fff;box-shadow:0 1px 3px rgba(0,0,0,.5)}
.dots{left:157px;top:446px;display:flex;gap:3px}
.dots i{width:12px;height:12px;border-radius:50%;background:#eee;border:1px solid #888}
.dots i:first-child{background:var(--red)}
.slider-shadow{left:170px;top:474px;width:480px;height:18px;background:radial-gradient(ellipse at top,rgba(0,0,0,.35),rgba(0,0,0,0) 70%)}

.news{left:678px;top:190px;width:229px;height:284px;background:#e9e9e9}
.news h3{position:absolute;left:10px;top:16px;font-size:12px;font-weight:400;color:#333}
.news-item{position:absolute;left:0;width:229px;height:54px;background:linear-gradient(#f7f7f7,#e4e4e4);border-top:1px solid #d0d0d0;padding:12px 10px;font-size:9px;line-height:12px;color:#333}
.news-ctrl{left:843px;top:454px;display:flex;gap:6px}

/* info boxes */
.info-box{top:510px;width:243px;height:138px;background:var(--panel);border:1px solid #ddd;border-radius:3px}
.info-box h3{position:absolute;top:10px;width:100%;text-align:center;font-size:12px;font-weight:400}
.info-img{position:absolute;left:10px;top:40px;width:75px;height:75px;border:1px solid #ccc}
.info-box p{position:absolute;left:94px;top:43px;width:140px;font-size:8.5px;line-height:11px;color:#444}
.btn-dark{background:linear-gradient(#3a72bb,#1e4f96);color:#fff;border-radius:3px;font-size:9px;text-align:center;line-height:16px;height:16px;width:72px}
.info-box .btn-dark{position:absolute;right:12px;top:111px}

/* welcome */
.welcome-title{left:165px;top:668px;font-size:20px;color:#333}
.welcome-title b{font-weight:400;color:var(--blue)}
.welcome-rule{left:165px;top:707px;width:480px;height:1px;background:var(--line)}
.welcome-img{left:168px;top:745px;width:147px;height:110px;border:4px solid #eee;box-shadow:0 0 2px #aaa;background:linear-gradient(120deg,#e6ecf2,#9fb0c0 60%,#50606f)}
.welcome-text{left:334px;top:750px;width:308px;font-size:10px;line-height:13.5px;color:#444;text-indent:20px}
.read-more-grey{left:556px;top:870px;width:71px;height:23px;line-height:23px;background:linear-gradient(#777,#4a4a4a);color:#fff;border-radius:3px;font-size:11px;text-align:center}

.testimonial{left:150px;top:933px;width:512px;height:148px;background:var(--panel);border:1px solid #ddd;border-radius:3px}
.testimonial h3{position:absolute;left:26px;top:11px;font-size:18px;font-weight:400}
.testi-photo{position:absolute;left:26px;top:46px;width:75px;height:72px;border:3px solid #fff;box-shadow:0 0 2px #999;background:linear-gradient(#c9d3dc,#6f7f8d)}
.quote{position:absolute;font-size:28px;color:var(--navy);font-family:Georgia,serif}
.testimonial p{position:absolute;left:134px;top:55px;width:335px;font-size:9px;line-height:11.5px;color:#444}
.testi-name{position:absolute;left:134px;top:87px;font-size:9px;line-height:11px;color:var(--red)}
.find-more{position:absolute;left:385px;top:128px;font-size:9px;color:#333}

/* recent articles */
.articles{left:675px;top:665px;width:228px;height:337px;background:var(--panel);border:1px solid #ddd;border-radius:3px}
.articles h3{position:absolute;left:12px;top:9px;font-size:11px;font-weight:400}
.article{position:absolute;left:0;width:226px;height:70px;border-top:1px solid #d8d8d8}
.article .thumb{position:absolute;left:13px;top:10px;width:47px;height:48px;border:2px solid #fff;box-shadow:0 0 2px #999}
.article .t{position:absolute;left:75px;top:6px;font-size:8.5px;font-weight:700;color:#333}
.article .s{position:absolute;left:75px;top:18px;width:145px;font-size:8.5px;line-height:10.5px;color:#444}
.article .m{position:absolute;left:75px;top:43px;font-size:8px;color:#444}
.article .m b,.view-all{color:var(--red);font-weight:400}
.view-all{position:absolute;left:180px;top:323px;font-size:9px;text-decoration:underline}

.newsletter{left:675px;top:1012px;width:228px;height:68px;background:linear-gradient(#1a6aa8,#0f4a80);border-radius:4px;color:#fff}
.newsletter h3{position:absolute;left:12px;top:5px;font-size:12px;font-weight:400}
.newsletter .sub{position:absolute;left:0;width:100%;text-align:center;top:22px;font-size:9px}
.newsletter .field{position:absolute;left:8px;top:38px;width:125px;height:22px;background:#fff;color:#444;font-size:9px;padding:5px 6px;border-radius:2px}
.newsletter .go{position:absolute;left:138px;top:38px;width:82px;height:22px;background:linear-gradient(#fff,#ccc);color:#333;font-size:10px;text-align:center;line-height:22px;border-radius:3px}

/* footer */
.footer-links{left:142px;top:1099px;width:768px;text-align:center;font-size:9.5px;color:#fff}
.footer-links span{margin:0 4px}
.footer-rule{left:142px;top:1121px;width:768px;height:1px;background:#555}
.follow{left:430px;top:1135px;display:flex;align-items:center;gap:4px;color:#fff;font-size:11px}
.follow i{display:block;width:22px;height:22px;border-radius:4px;margin-left:2px}
.copyright{left:0;top:1178px;width:1050px;text-align:center;color:#fff;font-size:11px}
</style>
</head>
<body>
<div class="page"></div>

<header>
  <div class="abs account-tab"><span>Register</span>|<span>Sign Up</span>|<span>Sign In</span></div>
  <div class="abs flags">
    <svg width="18" height="12" aria-label="English"><rect width="18" height="12" fill="#1f3a8a"/><rect x="7" width="4" height="12" fill="#fff"/><rect y="4" width="18" height="4" fill="#fff"/><rect x="8" width="2" height="12" fill="#c8102e"/><rect y="5" width="18" height="2" fill="#c8102e"/></svg>
    <svg width="18" height="12" aria-label="Nederlands"><rect width="18" height="4" fill="#ae1c28"/><rect y="4" width="18" height="4" fill="#fff"/><rect y="8" width="18" height="4" fill="#21468b"/></svg>
  </div>
  <div class="abs logo-box"></div>
  <div class="abs logo-mark"></div>
  <div class="abs logo-name">BoltNet</div>
  <div class="abs social" aria-label="Social links">
    <i style="background:#3b5998"></i><i style="background:#3fb3e8"></i><i style="background:#2a77b6"></i><i style="background:#f29322"></i>
  </div>
  <div class="abs search">Search
    <svg width="16" height="16" viewBox="0 0 16 16"><circle cx="6.5" cy="6.5" r="4.5" fill="none" stroke="#2a7dc0" stroke-width="2"/><line x1="10" y1="10" x2="14.5" y2="14.5" stroke="#2a7dc0" stroke-width="3" stroke-linecap="round"/></svg>
  </div>
  <nav class="abs main-nav">
    <a style="width:102px">HOME</a><a style="width:122px">SERVICES</a><a style="width:143px">REFERENCES</a><a style="width:105px">NEWS</a><a style="width:153px">ABOUT BOLTNET</a><a style="width:143px;border:0">CONTACT</a>
  </nav>
</header>

<section>
  <div class="abs slider"></div>
  <div class="abs slide-photo" role="img" aria-label="Businessman in a suit holding a laptop in a bright office"></div>
  <div class="abs slide-title">LOREM IPSUM DOLOR SIT AMET CONSECTETEUR ADIPSICING</div>
  <div class="abs slide-text">Lorem ipsum dolor sit amet, consecteteur adipiscing elit. Set diem nonumy. In convalis gravida neque. Nulla...</div>
  <div class="abs btn-blue slide-more">read more</div>
  <svg class="abs arrow" style="left:147px;top:308px" viewBox="0 0 30 30"><path d="M18 8 L11 15 L18 22" fill="none" stroke="#444" stroke-width="3"/></svg>
  <svg class="abs arrow" style="left:642px;top:308px" viewBox="0 0 30 30"><path d="M12 8 L19 15 L12 22" fill="none" stroke="#444" stroke-width="3"/></svg>
  <div class="abs dots"><i></i><i></i><i></i><i></i><i></i></div>
  <div class="abs slider-shadow"></div>

  <aside class="abs news">
    <h3>LATEST NEWS</h3>
    <div class="news-item" style="top:38px">Lorem ipsum dolor sit amet, consecteteur adipis cing elit. In convalis gravida neque.</div>
    <div class="news-item" style="top:92px;height:56px">Lorem ipsum dolor sit amet, consecteteur adipis cing elit. In convalis gravida neque.</div>
    <div class="news-item" style="top:148px;height:56px">Lorem ipsum dolor sit amet, consecteteur adipis cing elit. In convalis gravida neque.</div>
    <div class="news-item" style="top:204px;height:56px">Lorem ipsum dolor sit amet, consecteteur adipis cing elit. In convalis gravida neque.</div>
  </aside>
  <svg class="abs news-ctrl" width="46" height="12" viewBox="0 0 46 12"><path d="M0 6 L8 1 L8 11Z" fill="#888"/><rect x="19" y="1" width="2.5" height="10" fill="#888"/><rect x="24" y="1" width="2.5" height="10" fill="#888"/><path d="M46 6 L38 1 L38 11Z" fill="#888"/></svg>
</section>

<section>
  <div class="abs info-box" style="left:150px"><h3>HOW IT WORKS?</h3>
    <div class="info-img" role="img" aria-label="Hand touching a digital screen" style="background:linear-gradient(135deg,#f4f4f4,#c7c9cc)"></div>
    <p>Lorem ipsum dolor sit amet, con secteteur adipiscing elit. Set diem nonumy, in convalis gravida neq ue. Nulla gravida vestibulum me tis a acumsan</p><div class="btn-dark">read more &gt;&gt;</div></div>
  <div class="abs info-box" style="left:405px"><h3>YOUR BUSINESES NEEDS</h3>
    <div class="info-img" role="img" aria-label="Business team at a meeting table" style="background:linear-gradient(135deg,#e8e2da,#8f7b6a)"></div>
    <p>Lorem ipsum dolor sit amet, con secteteur adipiscing elit. Set diem nonumy, in convalis gravida neq ue. Nulla gravida vestibulum me tis a acumsan</p><div class="btn-dark">read more &gt;&gt;</div></div>
  <div class="abs info-box" style="left:660px"><h3>OUR SERVICES</h3>
    <div class="info-img" role="img" aria-label="Professional on the phone" style="background:linear-gradient(135deg,#caa27a,#4a3a30)"></div>
    <p>Lorem ipsum dolor sit amet, con secteteur adipiscing elit. Set diem nonumy, in convalis gravida neq ue. Nulla gravida vestibulum me tis a acumsan</p><div class="btn-dark">read more &gt;&gt;</div></div>
</section>

<main>
  <h1 class="abs welcome-title" style="font-weight:400">Welcome To <b>BoltNet</b></h1>
  <div class="abs welcome-rule"></div>
  <div class="abs welcome-img" role="img" aria-label="Smiling business team in an office"></div>
  <p class="abs welcome-text">Lorem ipsum dolor sit amet, consectetur adipiscing elit. set diem nonumy in convalis gravida neque. Nulla gravida vestibulum metis a acumsan, aliquam in sagitis ut. Solicitudin sed massa ud enim veniam. Curabitur tempus sem vitae mi vestibulum volutpat malesuada erat vestibulum. Sed aliquam dolor at dolor consequat gravida. Fusce mineque tempus nec fequat sit amet . Tincidunt ut leo. Nam semper omare enim.</p>
  <div class="abs read-more-grey">Read more</div>

  <div class="abs testimonial"><h3>Testimonial</h3>
    <div class="testi-photo" role="img" aria-label="Portrait of a client"></div>
    <span class="quote" style="left:118px;top:20px">&ldquo;</span>
    <p>Lorem ipsum dolor sit amet, consectetur adipiscing elit. set diem nonumy in convalis gravida neque. Nulla gravida vestibulum metis a acumsan, aliquam in sagitis ut.</p>
    <span class="quote" style="left:430px;top:58px">&rdquo;</span>
    <div class="testi-name">John Doe, Whoever CEO<br>Washington</div>
    <div class="find-more"><u>Find out more</u> &gt;&gt;</div>
  </div>
</main>

<aside class="abs articles"><h3>RECENT ARTICLES</h3>
  <div class="article" style="top:30px"><div class="thumb" role="img" aria-label="Keyboard close-up" style="background:linear-gradient(#9bc4e6,#2d5f8f)"></div><div class="t">Lorem ipsum dolor sit amet</div><div class="s">Lorem ipsum dolor sit amet,conse ctetuer adipiscing elit. set ...</div><div class="m"><b>posted</b> on july 15th 2012 | <b>Read more</b></div></div>
  <div class="article" style="top:100px"><div class="thumb" role="img" aria-label="Businessman at a laptop" style="background:linear-gradient(#e4e8ec,#4a4f58)"></div><div class="t">Lorem ipsum dolor sit amet</div><div class="s">Lorem ipsum dolor sit amet,conse ctetuer adipiscing elit. set ...</div><div class="m"><b>posted</b> on july 15th 2012 | <b>Read more</b></div></div>
  <div class="article" style="top:170px"><div class="thumb" role="img" aria-label="Blue network technology" style="background:linear-gradient(#3a8fd0,#0b2f5a)"></div><div class="t">Lorem ipsum dolor sit amet</div><div class="s">Lorem ipsum dolor sit amet,conse ctetuer adipiscing elit. set ...</div><div class="m"><b>posted</b> on july 15th 2012 | <b>Read more</b></div></div>
  <div class="article" style="top:240px"><div class="thumb" role="img" aria-label="Business handshake" style="background:linear-gradient(#f0f0f0,#8a7a70)"></div><div class="t">Lorem ipsum dolor sit amet</div><div class="s">Lorem ipsum dolor sit amet,conse ctetuer adipiscing elit. set ...</div><div class="m"><b>posted</b> on july 15th 2012 | <b>Read more</b></div></div>
  <div class="view-all">View All</div>
</aside>

<div class="abs newsletter"><h3>Newsletter Sign Up</h3><div class="sub">Receive update news from us weekly</div><div class="field">Your email address</div><div class="go">SUBSCRIBE</div></div>

<footer>
  <div class="abs footer-links">Home<span>|</span>Services<span>|</span>References<span>|</span>About BoltNet<span>|</span>Testimonials<span>|</span>Latest News<span>|</span>Recent Articles<span>|</span>Sitemap<span>|</span>Register<span>|</span>Sign In<span>|</span>Contact Us</div>
  <div class="abs footer-rule"></div>
  <div class="abs follow">FOLLOW US ON :<i style="background:#3b5998"></i><i style="background:#3fb3e8"></i><i style="background:#2a77b6"></i><i style="background:#f29322"></i></div>
  <div class="abs copyright">Copyright &copy; 2012, BoltNet.com. All rights reserved.</div>
</footer>
</body>
</html>
```